Business Card - Rebranding for Consulting Firm

We are renaming and rebranding our consulting firm and need to raise the level of quality of our cards as part of that effort. We consult to leading high tech, life science and other innovation sector companies.

Need a two-sided business card design.

Side 1: (a) Company logo (b) tag line: Optimize Your Investment in Talent (c) Name (d) Title (e) Phone 1: Office (f) Phone 2: Mobile (g) email: person@HollowmereAdvisory.com

Side 2: Two lines of text: (a) Growth is Imperative. Change is Constant. Talent Executes Strategy. (b) We help you excel at all three.

Target Market(s)

Business and human resources executives and senior managers

Industry/Entity Type

Management Consulting

Contact Information for Business Card

Font styles to use
Sans Serif

Requirements
Must have
• clean, not too busy, but with a bit of creativity. Stick to the colors used in the attached logo
• appeal to high tech, life science companies
Nice to have
• prefer white background

```html
<!DOCTYPE html>
<html lang="en">
<head>
<meta charset="utf-8">
<title>Hollowmere Advisory – Business Card</title>
<link rel="stylesheet" href="https://fonts.googleapis.com/css2?family=Roboto:wght@400;500;700&display=swap">
<style>
  :root {
    --page-bg: #e6e7e9;
    --card-bg: #ffffff;
    --brand-blue: #1a6aa0;
    --sky-blue: #1ba1dc;
    --mid-blue: #138fc4;
    --text-grey: #555a5f;
    --rule-grey: #dcdfe2;
    --card-shadow: rgba(0, 0, 0, 0.28);
  }
  * { box-sizing: border-box; margin: 0; padding: 0; }
  html, body {
    width: 1200px;
    height: 1000px;
    overflow: hidden;
    background: var(--page-bg);
    font-family: "Roboto", Arial, sans-serif;
  }
  .canvas { position: relative; width: 1200px; height: 1000px; }

  .card {
    position: absolute;
    left: 220px;
    width: 761px;
    background: var(--card-bg);
    box-shadow: 0 4px 14px var(--card-shadow);
    overflow: hidden;
  }
  .card--message { top: 50px; height: 434px; }
  .card--contact { top: 524px; height: 436px; }

  .wordmark {
    display: flex;
    align-items: center;
    gap: 12px;
    color: var(--brand-blue);
    font-weight: 500;
    font-size: 38px;
    letter-spacing: -0.5px;
    white-space: nowrap;
  }
  .wordmark__square {
    width: 28px;
    height: 28px;
    background: var(--brand-blue);
    flex: none;
  }

  /* Message side */
  .card--message .wordmark {
    position: absolute;
    top: 146px;
    left: 0;
    right: 0;
    justify-content: center;
  }
  .message-rule {
    position: absolute;
    top: 236px;
    left: 76px;
    width: 607px;
    height: 1px;
    background: var(--rule-grey);
  }
  .pillars {
    position: absolute;
    top: 262px;
    left: 0;
    right: 0;
    text-align: center;
    font-size: 18px;
    color: var(--text-grey);
    letter-spacing: 0.2px;
  }
  .pillars__sep { color: var(--sky-blue); margin: 0 8px; }
  .promise {
    position: absolute;
    top: 298px;
    left: 0;
    right: 0;
    text-align: center;
    font-size: 18px;
    color: var(--text-grey);
    letter-spacing: 0.3px;
  }

  /* Contact side */
  .card--contact .wordmark {
    position: absolute;
    top: 52px;
    left: 53px;
  }
  .tagline {
    position: absolute;
    top: 126px;
    left: 53px;
    font-size: 18px;
    color: var(--sky-blue);
    letter-spacing: 1.6px;
  }
  .person { position: absolute; top: 218px; left: 53px; }
  .person__name {
    font-size: 23px;
    font-weight: 700;
    color: var(--brand-blue);
    line-height: 28px;
  }
  .person__title {
    font-size: 17px;
    color: var(--text-grey);
    line-height: 22px;
  }
  .contacts {
    position: absolute;
    top: 290px;
    left: 53px;
    list-style: none;
  }
  .contacts__item {
    display: flex;
    align-items: center;
    gap: 7px;
    font-size: 17.5px;
    color: var(--text-grey);
    line-height: 24px;
  }
  .contacts__icon { width: 13px; height: 13px; flex: none; }
  .corner-accent {
    position: absolute;
    right: 0;
    bottom: 0;
    width: 311px;
    height: 156px;
  }
</style>
</head>
<body>
<main class="canvas">

  <section class="card card--message" aria-label="Card back">
    <div class="wordmark"><span class="wordmark__square"></span>Hollowmere Advisory</div>
    <div class="message-rule"></div>
    <p class="pillars">Growth is Imperative<span class="pillars__sep">|</span>Change is Constant<span class="pillars__sep">|</span>Talent Executes Strategy</p>
    <p class="promise">We help you excel at all three.</p>
  </section>

  <section class="card card--contact" aria-label="Card front">
    <div class="wordmark"><span class="wordmark__square"></span>Hollowmere Advisory</div>
    <p class="tagline">Optimize Your Investment in Talent</p>

    <div class="person">
      <p class="person__name">Elliot Varga</p>
      <p class="person__title">National Director</p>
    </div>

    <ul class="contacts">
      <li class="contacts__item">
        <svg class="contacts__icon" viewBox="0 0 13 13"><rect x="3" y="0.5" width="7" height="12" rx="1.2" fill="none" stroke="var(--sky-blue)" stroke-width="1.4"/><circle cx="6.5" cy="10.5" r="0.8" fill="var(--sky-blue)"/></svg>
        0123 456 789
      </li>
      <li class="contacts__item">
        <svg class="contacts__icon" viewBox="0 0 13 13"><path d="M3 1 L5 3.5 L3.8 5 Q5.5 8 8 9.2 L9.5 8 L12 10 L10.5 12 Q4 11 1 3 Z" fill="var(--sky-blue)"/></svg>
        0123 456 789
      </li>
      <li class="contacts__item">
        <svg class="contacts__icon" viewBox="0 0 13 13"><rect x="0.5" y="2.5" width="12" height="8" fill="var(--sky-blue)"/><path d="M0.5 2.5 L6.5 7 L12.5 2.5" fill="none" stroke="#fff" stroke-width="1"/></svg>
        person@HollowmereAdvisory.com
      </li>
      <li class="contacts__item">
        <svg class="contacts__icon" viewBox="0 0 13 13"><g fill="none" stroke="var(--sky-blue)" stroke-width="1.1"><circle cx="6.5" cy="6.5" r="5.5"/><ellipse cx="6.5" cy="6.5" rx="2.4" ry="5.5"/><line x1="1" y1="6.5" x2="12" y2="6.5"/></g></svg>
        www.HollowmereAdvisory.com
      </li>
    </ul>

    <svg class="corner-accent" viewBox="0 0 311 156" role="img" aria-label="Decorative blue corner accent echoing the brand mark">
      <defs>
        <linearGradient id="cornerFill" x1="0" y1="0" x2="1" y2="0">
          <stop offset="0" stop-color="var(--sky-blue)"/>
          <stop offset="1" stop-color="var(--brand-blue)"/>
        </linearGradient>
      </defs>
      <polygon points="0,156 311,0 311,156" fill="url(#cornerFill)"/>
    </svg>
  </section>

</main>
</body>
</html>
```